Kestrel Garment Company "Sale Flyer"

We need flyer for a company selling clothing, the purpose of the flyer is advertising the available product. This flyer has to be specific for the product category of "men shorts". The flyer should be attractive and will have to feature pictures of the product which are attached. Furthermore, the flyer should feature the company name and logo. The company name is Kestrel Garment Company. The flyer should mention that the product is manufactured in a facility rated Platinum under the VORA Eco Structure Grading Scheme hence the damage to the environment is nill because of the product.The flyer should mention the address of the store No. 52, Fourth Lane Road, Colombo 11, Sri Lanka. The telephone number +94 71 508 3947. The product price also should be mentioned prominently which is "Rs. 790". Flyer size should be A4 front only. Many pictures are attached of course all cannot be used, looking forward to an attractive flyer. Thank you.

Target Market(s)

Men age 16 - 45

Industry/Entity Type

Clothing

Requirements
Must have
• Logo : in the attachment
• Contact number : +94 71 508 3947
• Address : No. 52, Fourth Lane Road, Colombo 11, Sri Lanka.
• Price : Rs. 790

```html
<!DOCTYPE html>
<html lang="en">
<head>
<meta charset="utf-8">
<title>Kestrel Garment Company – Man Shorts Flyer</title>
<link rel="stylesheet" href="https://fonts.googleapis.com/css2?family=Open+Sans:wght@400;600;700;800&display=swap">
<style>
  :root {
    --page-light: #d9d9d9;
    --page-mid: #8c8c8c;
    --page-dark: #3a3a3c;
    --panel-dark: #2c2d30;
    --logo-box: #3b3a37;
    --logo-text: #f4efe4;
    --banner: #cfcfcf;
    --white: #ffffff;
    --tag: #f3ecdc;
    --tag-text: #2b2b2b;
    --badge: #e8e8e8;
  }
  * { margin: 0; padding: 0; box-sizing: border-box; }
  html, body { width: 849px; height: 1200px; overflow: hidden; }
  body { font-family: "Open Sans", Arial, sans-serif; }

  .flyer {
    position: relative;
    width: 849px;
    height: 1200px;
    overflow: hidden;
    background: linear-gradient(100deg, var(--page-light) 0%, var(--page-mid) 30%, var(--page-dark) 45%, var(--panel-dark) 100%);
  }

  .brand {
    position: absolute;
    left: 80px; top: 14px;
    width: 196px; height: 150px;
    background: var(--logo-box);
    display: flex; align-items: center; justify-content: center;
    text-align: center;
    padding: 12px;
  }
  .brand-name {
    color: var(--logo-text);
    font-weight: 700;
    font-size: 26px;
    line-height: 1.15;
  }

  .title-band {
    position: absolute;
    left: 306px; top: 34px;
    width: 543px; height: 72px;
    background: linear-gradient(90deg, var(--banner), #eeeeee);
    display: flex; align-items: center; justify-content: center;
  }
  .title-band h1 {
    color: var(--white);
    font-weight: 800;
    font-size: 40px;
    letter-spacing: 1px;
    text-shadow: 0 1px 3px rgba(0,0,0,0.45);
  }

  .range {
    position: absolute;
    left: 50px; top: 182px;
    width: 275px;
  }
  .range-row {
    display: flex; gap: 6px;
    height: 212px;
    margin-bottom: 42px;
  }
  .range-row:last-child { margin-bottom: 0; }
  .swatch { flex: 1; border-radius: 2px; }
  .navy { background: linear-gradient(180deg, #3f4d6a, #2c3850); }
  .plaid { background: linear-gradient(135deg, #9fb2cc, #e3ddc8 55%, #7f93b6); }
  .brown { background: linear-gradient(180deg, #7a6a58, #5e5142); }
  .blush { background: linear-gradient(180deg, #e1c7c0, #c9aea6); }
  .cyan { background: linear-gradient(180deg, #3bb7e6, #1d97cc); }
  .grey { background: linear-gradient(180deg, #a3a4a6, #7f8083); }
  .rose { background: linear-gradient(180deg, #c2515e, #a13845); }
  .red { background: linear-gradient(180deg, #e8232c, #c7141d); }

  .hero-photo {
    position: absolute;
    left: 345px; top: 113px;
    width: 490px; height: 560px;
    background: linear-gradient(160deg, #ebe7dc 0%, #d9d4c6 25%, #5a6f90 40%, #435675 75%, #374762 100%);
  }

  .price-tag {
    position: absolute;
    left: 420px; top: 245px;
    width: 200px; height: 125px;
  }
  .price-tag svg { position: absolute; inset: 0; }
  .price-tag .price {
    position: absolute;
    left: 40px; top: 36px;
    transform: rotate(-14deg);
    color: var(--tag-text);
    font-weight: 800;
    font-size: 46px;
    line-height: 1;
    white-space: nowrap;
  }
  .price-tag .price small { font-size: 22px; font-weight: 700; }

  .contact {
    position: absolute;
    left: 404px;
    color: var(--white);
    display: flex; align-items: flex-start; gap: 16px;
  }
  .contact.phone { top: 704px; }
  .contact.address { top: 862px; }
  .contact svg { flex: none; }
  .contact-text { font-weight: 600; line-height: 1.3; }
  .phone .contact-text { font-size: 32px; padding-top: 2px; }
  .address .contact-text { font-size: 23px; padding-top: 8px; }

  .eco-note {
    position: absolute;
    left: 396px; top: 995px;
    width: 320px;
    color: var(--white);
    font-size: 14.5px;
    line-height: 1.35;
  }

  .eco-badge {
    position: absolute;
    left: 728px; top: 992px;
    width: 100px; height: 100px;
    border-radius: 50%;
    background: var(--badge);
  }
</style>
</head>
<body>
<main class="flyer">
  <header class="brand">
    <span class="brand-name">Kestrel Garment Company</span>
  </header>

  <div class="title-band"><h1>MAN SHORTS</h1></div>

  <section class="range" aria-label="Shorts colour range">
    <div class="range-row">
      <div class="swatch navy" role="img" aria-label="Navy chino shorts"></div>
      <div class="swatch plaid" role="img" aria-label="Blue and beige check shorts"></div>
    </div>
    <div class="range-row">
      <div class="swatch brown" role="img" aria-label="Brown chino shorts"></div>
      <div class="swatch blush" role="img" aria-label="Light pink chino shorts"></div>
    </div>
    <div class="range-row">
      <div class="swatch cyan" role="img" aria-label="Bright blue shorts"></div>
      <div class="swatch grey" role="img" aria-label="Grey shorts"></div>
    </div>
    <div class="range-row">
      <div class="swatch rose" role="img" aria-label="Dusty red shorts"></div>
      <div class="swatch red" role="img" aria-label="Red shorts"></div>
    </div>
  </section>

  <div class="hero-photo" role="img" aria-label="Blue chambray men's shorts laid over beige shorts"></div>

  <div class="price-tag">
    <svg width="200" height="125" viewBox="0 0 200 125">
      <polygon points="14,50 168,10 194,82 40,120 6,90" fill="var(--tag)"/>
      <circle cx="24" cy="72" r="5" fill="#555"/>
    </svg>
    <div class="price"><small>Rs.</small> 790</div>
  </div>

  <div class="contact phone">
    <svg width="44" height="44" viewBox="0 0 44 44" aria-hidden="true">
      <rect x="12" y="4" width="20" height="36" rx="3" fill="none" stroke="#fff" stroke-width="3"/>
      <line x1="18" y1="34" x2="26" y2="34" stroke="#fff" stroke-width="3"/>
    </svg>
    <span class="contact-text">+94 71 508 3947</span>
  </div>

  <div class="contact address">
    <svg width="44" height="56" viewBox="0 0 44 56" aria-hidden="true">
      <path d="M22 4 C11 4 4 12 4 22 C4 35 22 52 22 52 C22 52 40 35 40 22 C40 12 33 4 22 4 Z" fill="#fff"/>
      <circle cx="22" cy="21" r="7" fill="var(--panel-dark)"/>
    </svg>
    <span class="contact-text">No. 52, Fourth Lane Road,<br>Colombo 11, Sri Lanka</span>
  </div>

  <p class="eco-note">the product is manufactured in a facility rated Platinum under the VORA Eco Structure Grading Scheme hence the damage to the environment is nill because of the product.</p>

  <div class="eco-badge" aria-hidden="true"></div>
</main>
</body>
</html>
```